Lifecoach needs website design based on a standard Wordpress theme

I need a website for my new lifecoaching business that can be easily implemented in Wordpress, it needs to be compatible with a standard Wordpress theme. So I can place the pictures, texts etc. in a standard theme of Wordpress.

I want the design to be a very good feeling and playfull one, based on my logo.

Target Market(s)

I will coach people to reach their goals and dreams in life.

Industry/Entity Type

Business

Requirements
Must have
• Can be easy implemented in Wordpress.
Nice to have
• Photo's of nature are nice.

```html
<!DOCTYPE html>
<html lang="en">
<head>
<meta charset="utf-8">
<title>Lena ter Horst – Lifecoach</title>
<link href="https://fonts.googleapis.com/css2?family=PT+Sans:wght@400;700&family=Arimo:wght@400;700&display=swap" rel="stylesheet">
<style>
:root{
  --bg:#e5eed9;
  --footer-bg:#dde7cc;
  --top-bar:#8aad2a;
  --brand-green:#6f9a2e;
  --ink:#1f2a14;
  --nav:#2d3322;
  --accent:#ec6608;
  --muted:#8c9583;
  --footer-head:#7d8673;
  --footer-link:#9aa391;
  --rule:#d3dcc5;
  --tile-1:#6c9150;
  --tile-2:#779f4d;
  --tile-3:#86a84f;
  --tile-4:#93b353;
}
*{box-sizing:border-box;margin:0;padding:0}
html,body{width:929px;height:1200px;overflow:hidden}
body{background:var(--bg);font-family:"Arimo",Arial,sans-serif;position:relative;color:var(--muted)}
.top-bar{position:absolute;left:0;top:0;width:929px;height:13px;background:var(--top-bar)}
.brand{position:absolute;left:142px;top:54px;font-family:"PT Sans",sans-serif;font-weight:400;color:var(--brand-green);font-size:22px;line-height:1}
.main-nav{position:absolute;top:68px;right:138px;display:flex;gap:14px;font-size:10.5px;color:var(--nav)}
.main-nav .current{color:var(--accent)}
.gallery{position:absolute;left:140px;top:102px;width:651px;display:grid;grid-template-columns:repeat(4,1fr);column-gap:12px}
.photo{height:287px}
.photo-ladybird{background:linear-gradient(160deg,#2f7a10,#7cc42a 55%,#3f8c16)}
.photo-bird{background:radial-gradient(circle at 55% 40%,#fff 0,#7fb6f0 18%,#1a62c8 55%,#0b3f9e)}
.photo-stones{background:radial-gradient(circle at 50% 45%,#e9e4dc,#bcb3a6 60%,#8c8275)}
.photo-garden{background:linear-gradient(180deg,#56663f,#c9d0c3 40%,#6f7c49 70%,#b8462f)}
.tile{margin-top:6px;height:98px;padding:20px 13px;color:#fff}
.tile h3{font-family:"PT Sans",sans-serif;font-size:14px;font-weight:700;margin-bottom:6px;letter-spacing:-.2px}
.tile p{font-size:9px;line-height:1.3;color:#e6efd6}
.tile-1{background:var(--tile-1)}.tile-2{background:var(--tile-2)}.tile-3{background:var(--tile-3)}.tile-4{background:var(--tile-4)}
.intro{position:absolute;left:142px;top:527px;width:460px}
.intro h1{font-family:"PT Sans",sans-serif;font-size:22px;color:var(--ink);font-weight:700;margin-bottom:6px;letter-spacing:-.3px}
.intro p{font-size:9px;font-style:italic;line-height:1.6}
.contact-btn{position:absolute;left:652px;top:529px;width:139px;height:57px;background:var(--accent);color:#fff;font-family:"PT Sans",sans-serif;font-weight:700;font-size:15px;display:flex;align-items:center;justify-content:center}
.rule{position:absolute;left:0;top:625px;width:929px;height:1px;background:var(--rule)}
.section-title{font-family:"PT Sans",sans-serif;font-weight:700;font-size:19px;color:var(--ink);text-transform:uppercase}
.copy{font-size:9.8px;line-height:1.45}
.more-btn{display:inline-block;background:var(--accent);color:#fff;font-size:7px;font-weight:700;padding:7px 9px;text-transform:uppercase}
.welcome{position:absolute;left:142px;top:660px;width:368px}
.welcome .copy{margin:14px 0 10px}
.about{position:absolute;left:143px;top:808px;width:368px}
.about .copy{margin:0 0 10px -1px}
.testimonials{position:absolute;left:586px;top:655px;width:205px}
.quote-icon{flex:none;width:58px;height:58px;border-radius:50%;background:var(--accent);color:#fff;font-family:"PT Sans",sans-serif;font-weight:700;font-size:70px;line-height:92px;text-align:center}
.testimonial-body{display:flex;gap:13px;margin-top:12px}
.testimonials .copy p+p{margin-top:13px}
.testimonials .more-btn{margin:10px 0 0 161px}
.who-we-are{position:absolute;left:585px;top:834px;width:207px}
.who-we-are .testimonial-body{margin-top:4px;align-items:flex-start}
.who-we-are .copy{width:136px;margin-left:4px;margin-top:2px}
.site-footer{position:absolute;left:0;top:956px;width:929px;height:244px;background:var(--footer-bg)}
.footer-cols{position:absolute;left:142px;top:38px;display:grid;grid-template-columns:166px 166px 166px 140px}
.footer-cols h4{font-family:"PT Sans",sans-serif;font-weight:700;font-size:14px;color:var(--footer-head);margin-bottom:15px}
.footer-cols li{list-style:none;font-size:9.5px;color:var(--footer-link);line-height:20.8px}
.footer-cols p{font-size:9.5px;color:var(--footer-link);line-height:1.45}
.to-top{position:absolute;left:812px;top:169px;width:80px;height:36px;background:var(--accent);color:#fff;font-size:8.5px;font-weight:700;display:flex;align-items:center;justify-content:center;gap:5px}
</style>
</head>
<body>
<div class="top-bar"></div>

<header>
  <div class="brand">Lena ter Horst Lifecoach</div>
  <nav class="main-nav">
    <span class="current">Main</span><span>About</span><span>Services</span><span>Projects</span><span>Blog</span><span>Contacts</span>
  </nav>
</header>

<section class="gallery">
  <div class="photo photo-ladybird" role="img" aria-label="Ladybird climbing a green grass stem"></div>
  <div class="photo photo-bird" role="img" aria-label="White bird flying in a bright blue sky"></div>
  <div class="photo photo-stones" role="img" aria-label="Stack of smooth zen stones on raked sand"></div>
  <div class="photo photo-garden" role="img" aria-label="Wooden bridge in a misty Japanese garden"></div>
  <div class="tile tile-1"><h3>Set Powerful Goals</h3><p>Lorem ipsum dolor sit amo nsec tetuer adipiscing elit.</p></div>
  <div class="tile tile-2"><h3>Building Confidence</h3><p>Praesent vestibulum molestie lacus. Aenean nonumm.</p></div>
  <div class="tile tile-3"><h3>Overcoming inhertia</h3><p>Lorem ipsum dolor sit amo nsec tetuer adipiscing elit.</p></div>
  <div class="tile tile-4"><h3>Free! Coaching</h3><p>Praesent vestibulum molestie lacus. Aenean nonumm.</p></div>
</section>

<section class="intro">
  <h1>We work to make a reality of your desire</h1>
  <p>Lorem ipsum dolor sit amo nsec tetuer adipiscing eliaesent vestibulum molestie lacus. Aenean nonummyeerit mauris. Phasellus porta. Fusce suscipit varius mi. Cum sociis natoque penatibus et magn.</p>
</section>
<div class="contact-btn">Contact Us</div>

<div class="rule"></div>

<section class="welcome">
  <h2 class="section-title">Welcome</h2>
  <p class="copy">Molestie lacus. Aenean nonummy hendrerit maurellus porta. Fusce sscipit varius me sociis natoque penatibet magss paurient montes naetu ridiculu musulla dui.<br>Fusce feugiat malesuada odio. Morbi nun odio gravda aursus necuctus a lorem. Maecenas tristique orci ac sem.</p>
  <span class="more-btn">More</span>
</section>

<section class="about">
  <h2 class="section-title">About Us</h2>
  <p class="copy">Molestie lacus. Aenean nonummy hendrerit maurellus porta. Fusce sscipit varius me sociis natoque penatibet magss paurient montes naetu ridiculu musulla dui.<br>Fusce feugiat malesuada odio. Morbi nun odio gravda aursus necuctus a lorem. Maecenas tristique orci ac sem.</p>
  <span class="more-btn">More</span>
</section>

<section class="testimonials">
  <h2 class="section-title">Testimonials</h2>
  <div class="testimonial-body">
    <div class="quote-icon">&ldquo;</div>
    <div class="copy" style="width:134px">
      <p>Fusce sscipit varius m sociis natoque penatibet ma rturient montes naetu ridiculu msulla dui. Fusce feulesuada odio.</p>
      <p>Morbi nunc odio grvda aursu ctus a lorem. Maecenas trque orci ac tricies pharetra.</p>
    </div>
  </div>
  <span class="more-btn">More</span>
</section>

<section class="who-we-are">
  <h2 class="section-title">Who We Are</h2>
  <div class="testimonial-body">
    <p class="copy">Fusce sscipit varius m sociis natoque penatibet ma rturient montes naetu ridiculu msulla dui. Fusce feulesuada odio.</p>
    <div class="quote-icon">&rdquo;</div>
  </div>
</section>

<footer class="site-footer">
  <div class="footer-cols">
    <div><h4>Categories</h4><ul><li>Aenean nonuy hendrerit</li><li>Cum sociis natoque pen</li><li>Fusce suscipit varius</li><li>Magnis dis parturient</li><li>Nascetur ridiculus mus</li></ul></div>
    <div><h4>Follow us</h4><ul><li>Microblog</li><li>Social Page</li><li>Community</li><li>Photo Stream</li></ul></div>
    <div><h4>Archive</h4><ul><li>August 2012</li><li>July 2012</li><li>June 2012</li><li>May 2012</li><li>April 2012</li></ul></div>
    <div><h4>Copyright</h4><p>Brightpath.net © 2014 • Privacy Policy</p></div>
  </div>
  <div class="to-top">
    <svg width="6" height="10" viewBox="0 0 6 10" aria-hidden="true"><path d="M3 10V1M0.5 3.5L3 1l2.5 2.5" stroke="#fff" stroke-width="1.2" fill="none"/></svg>
    to the top
  </div>
</footer>
</body>
</html>
```